Brightpine Heating and Cooling inc

Free System Replacement estimate
Financing available
Indoor Air Quality
high efficiency system
Zorvik, Pictaloom, Kindrafold
website info
Se Habla Espanol
Free second opinion
We service all major brand

Target Market(s)

Hvac Home Services

Industry/Entity Type

Hvac

Font styles to use
Sans Serif
Other font styles liked:
• Vorneq letter

Colors
3377b5
9bcb3c

```html
<!DOCTYPE html>
<html lang="en">
<head>
<meta charset="utf-8">
<title>Brightpine Heating and Cooling inc – Postcard</title>
<link href="https://fonts.googleapis.com/css2?family=Open+Sans:wght@400;600;700;800&family=Oswald:wght@500;700&display=swap" rel="stylesheet">
<style>
:root{
  --blue:#2e5a87;
  --green:#6cb83f;
  --white:#ffffff;
  --ink:#27466a;
  --line:#9aa6b2;
  --stage:#e3e4e5;
}
*{box-sizing:border-box;margin:0;padding:0}
html,body{width:1049px;height:1200px;overflow:hidden}
body{background:var(--stage);font-family:"Open Sans",Arial,sans-serif;position:relative}
.card{position:absolute;left:154px;width:740px;height:458px;background:var(--white);overflow:hidden;box-shadow:0 3px 8px rgba(0,0,0,.18)}
.card--front{top:112px}
.card--back{top:612px}
.card-shapes{position:absolute;left:0;top:0;width:740px;height:458px}
.abs{position:absolute}

.brand{display:flex;align-items:center;gap:10px;color:var(--blue);font-weight:800;line-height:1.05}
.brand-dot{border-radius:50%;background:var(--green);flex:none}
.brand--front{left:30px;top:26px}
.brand--front .brand-dot{width:58px;height:58px}
.brand--front .brand-name{font-size:30px}
.brand--front .brand-sub{font-size:15px}
.brand--back{left:441px;top:30px}
.brand--back .brand-dot{width:34px;height:34px}
.brand--back .brand-name{font-size:20px}
.brand--back .brand-sub{font-size:10px}

.tagline{color:var(--green);font-weight:700;letter-spacing:.2px;white-space:nowrap}
.headline{color:var(--white);font-weight:700;font-size:22.5px;line-height:27px;letter-spacing:.3px;white-space:nowrap}

.perk-list{left:22px;top:228px;list-style:none}
.perk{display:flex;align-items:center;gap:12px;height:34px;color:var(--green);font-weight:700;font-size:14px;line-height:15px}
.perk:last-child{height:44px}
.icon-box{width:28px;height:28px;border:1.2px solid var(--line);border-radius:3px;flex:none;display:flex;align-items:center;justify-content:center}

.phone{display:flex;align-items:center;gap:10px;color:var(--white);font-family:"Oswald",sans-serif;font-weight:500;font-size:39px;letter-spacing:1px;white-space:nowrap}
.contact{display:flex;align-items:center;gap:7px;color:var(--white);font-weight:700;font-size:12.5px;white-space:nowrap}

.services-title{left:26px;top:236px;color:var(--blue);font-weight:700;font-size:18px;letter-spacing:.3px}
.service-list{left:24px;top:264px;list-style:none;width:400px}
.service{display:flex;gap:10px;height:41px}
.service .icon-box{width:32px;height:32px}
.service-name{color:var(--green);font-weight:700;font-size:11px;line-height:12px}
.service-text{color:var(--ink);font-size:9px;line-height:11px}

.stamp{left:625px;top:21px;width:93px;height:82px;border:1.5px solid #b9bec3}
.address-line{left:443px;width:277px;height:0;border-top:1.2px solid #b9bec3}
</style>
</head>
<body>

<!-- FRONT -->
<section class="card card--front">
  <svg class="card-shapes" viewBox="0 0 740 458">
    <defs>
      <linearGradient id="frontPhoto" x1="0" y1="0" x2="0.3" y2="1">
        <stop offset="0" stop-color="#a5715b"/>
        <stop offset="0.45" stop-color="#5b5650"/>
        <stop offset="0.8" stop-color="#4b4a45"/>
        <stop offset="1" stop-color="#5f7d3c"/>
      </linearGradient>
    </defs>
    <path role="img" aria-label="Photo: technician servicing an outdoor air conditioning unit beside a brick wall, with a 24/7 emergency services badge" d="M385 0 H740 V403 H398 C428 270 422 120 385 0 Z" fill="url(#frontPhoto)"/>
    <path d="M380 0 C417 120 423 270 393 403" fill="none" stroke="var(--green)" stroke-width="7"/>
    <polygon points="0,121 418,121 430,213 0,213" fill="var(--blue)"/>
    <rect x="0" y="403" width="740" height="55" fill="var(--blue)"/>
    <polygon points="0,390 292,390 324,458 0,458" fill="var(--green)"/>
  </svg>

  <div class="abs brand brand--front">
    <span class="brand-dot"></span>
    <div><div class="brand-name">Brightpine</div><div class="brand-sub">Heating and Cooling inc</div></div>
  </div>

  <div class="abs tagline" style="left:20px;top:133px;font-size:15px">QUALITY THAT IS GUARANTEED</div>
  <h1 class="abs headline" style="left:20px;top:152px">Heating and Air Conditioning<br>Comfort Specialist</h1>

  <ul class="abs perk-list">
    <li class="perk"><span class="icon-box"><svg width="18" height="18" viewBox="0 0 18 18"><rect x="7" y="2" width="4" height="10" rx="2" fill="none" stroke="var(--blue)" stroke-width="1.4"/><circle cx="9" cy="14" r="3" fill="var(--green)"/></svg></span>FREE SYSTEM REPLACEMENT ESTIMATE</li>
    <li class="perk"><span class="icon-box"><svg width="18" height="18" viewBox="0 0 18 18"><path d="M2 9 L9 3 L16 9 M4 8 V16 H14 V8" fill="none" stroke="var(--green)" stroke-width="1.5"/><circle cx="9" cy="12" r="2" fill="var(--blue)"/></svg></span>FINANCING AVAILABLE</li>
    <li class="perk"><span class="icon-box"><svg width="18" height="18" viewBox="0 0 18 18"><rect x="2" y="4" width="14" height="10" rx="1.5" fill="none" stroke="var(--green)" stroke-width="1.5"/><circle cx="7" cy="9" r="2.5" fill="var(--blue)"/></svg></span>INDOOR AIR QUALITY</li>
    <li class="perk"><span class="icon-box"><svg width="18" height="18" viewBox="0 0 18 18"><path d="M2 9 L9 3 L16 9 M4 8 V16 H14 V8" fill="none" stroke="var(--green)" stroke-width="1.5"/><path d="M7 15 V11 M9 15 V10 M11 15 V11" stroke="var(--blue)" stroke-width="1.3"/></svg></span>HALVORA TECHNOLOGIES HIGH EFFICIENCY<br>ON THE BACKGROUND</li>
  </ul>

  <div class="abs phone" style="left:24px;top:398px">
    <svg width="32" height="40" viewBox="0 0 32 40"><rect x="7" y="2" width="20" height="36" rx="3" fill="none" stroke="var(--white)" stroke-width="3"/><rect x="2" y="12" width="9" height="18" rx="2" fill="var(--white)"/><circle cx="17" cy="33" r="1.8" fill="var(--white)"/></svg>
    407-555-0148
  </div>
  <div class="abs contact" style="left:340px;top:422px">
    <svg width="14" height="11" viewBox="0 0 14 11"><rect x="1" y="1" width="12" height="9" fill="none" stroke="var(--white)" stroke-width="1.3"/><path d="M1 1 L7 6 L13 1" fill="none" stroke="var(--white)" stroke-width="1.3"/></svg>
    sam@brightpine365.com
  </div>
  <div class="abs contact" style="left:543px;top:422px">
    <svg width="14" height="14" viewBox="0 0 14 14"><circle cx="7" cy="7" r="6" fill="none" stroke="var(--white)" stroke-width="1.2"/><ellipse cx="7" cy="7" rx="2.6" ry="6" fill="none" stroke="var(--white)" stroke-width="1"/><path d="M1 7 H13" stroke="var(--white)" stroke-width="1"/></svg>
    www.brightpine365.com
  </div>
</section>

<!-- BACK -->
<section class="card card--back">
  <svg class="card-shapes" viewBox="0 0 740 458">
    <defs>
      <linearGradient id="backPhoto" x1="0" y1="0" x2="1" y2="1">
        <stop offset="0" stop-color="#e9eae8"/>
        <stop offset="0.45" stop-color="#8b8f7a"/>
        <stop offset="0.8" stop-color="#5f7a3c"/>
        <stop offset="1" stop-color="#4a4b46"/>
      </linearGradient>
    </defs>
    <path role="img" aria-label="Photo: outdoor air conditioning unit, indoor furnace and thermostat beside a landscaped patio, with a 24/7 emergency services badge" d="M0 0 H370 C390 60 400 120 402 177 H0 Z" fill="url(#backPhoto)"/>
    <path d="M374 0 C398 70 410 140 410 225 C410 300 400 360 388 404" fill="none" stroke="var(--green)" stroke-width="5"/>
    <polygon points="0,177 427,177 418,225 0,225" fill="var(--blue)"/>
    <rect x="0" y="404" width="740" height="54" fill="var(--blue)"/>
    <polygon points="0,391 313,391 345,458 0,458" fill="var(--green)"/>
  </svg>

  <div class="abs tagline" style="left:166px;top:188px;font-size:15px">QUALITY THAT IS GUARANTEED</div>
  <div class="abs" style="left:166px;top:206px;color:var(--white);font-size:10px;font-weight:700;letter-spacing:.3px">LIC# CAC1049372</div>

  <h2 class="abs services-title">OUR SERVICES</h2>
  <ul class="abs service-list">
    <li class="service"><span class="icon-box"><svg width="20" height="20" viewBox="0 0 20 20"><rect x="4" y="3" width="12" height="15" rx="1.5" fill="none" stroke="var(--blue)" stroke-width="1.5"/><path d="M7 10 L9 12 L13 8" fill="none" stroke="var(--green)" stroke-width="1.8"/></svg></span>
      <div><div class="service-name">ANNUAL INSPECTIONS</div><div class="service-text">allows a technician to identify dirty coils and burned out contactors before<br>they cause long term damage to your system.</div></div></li>
    <li class="service"><span class="icon-box"><svg width="20" height="20" viewBox="0 0 20 20"><path d="M10 2 V18 M3 6 L17 14 M17 6 L3 14" stroke="var(--green)" stroke-width="1.6"/><circle cx="10" cy="10" r="3" fill="var(--blue)"/></svg></span>
      <div><div class="service-name">A/C INSTALLATION</div><div class="service-text">high quality installation of residential and commercial air conditioning with<br>the use of professional equipment .</div></div></li>
    <li class="service"><span class="icon-box"><svg width="20" height="20" viewBox="0 0 20 20"><circle cx="8" cy="8" r="4.5" fill="none" stroke="var(--green)" stroke-width="2"/><path d="M11 11 L17 17" stroke="var(--blue)" stroke-width="2.4"/></svg></span>
      <div><div class="service-name">SERVICE AND REPAIR</div><div class="service-text">full range of service and repair options of air conditioning systems,<br>ventilation systems, light commercial and residential split systems.</div></div></li>
  </ul>

  <div class="abs brand brand--back">
    <span class="brand-dot"></span>
    <div><div class="brand-name">Brightpine</div><div class="brand-sub">Heating and Cooling inc</div></div>
  </div>
  <div class="abs stamp"></div>
  <div class="abs address-line" style="top:176px"></div>
  <div class="abs address-line" style="top:225px"></div>
  <div class="abs address-line" style="top:274px"></div>

  <div class="abs phone" style="left:24px;top:399px">
    <svg width="32" height="40" viewBox="0 0 32 40"><rect x="7" y="2" width="20" height="36" rx="3" fill="none" stroke="var(--white)" stroke-width="3"/><rect x="2" y="12" width="9" height="18" rx="2" fill="var(--white)"/><circle cx="17" cy="33" r="1.8" fill="var(--white)"/></svg>
    407-555-0148
  </div>
  <div class="abs contact" style="left:340px;top:422px">
    <svg width="14" height="11" viewBox="0 0 14 11"><rect x="1" y="1" width="12" height="9" fill="none" stroke="var(--white)" stroke-width="1.3"/><path d="M1 1 L7 6 L13 1" fill="none" stroke="var(--white)" stroke-width="1.3"/></svg>
    sam@brightpine365.com
  </div>
  <div class="abs contact" style="left:543px;top:422px">
    <svg width="14" height="14" viewBox="0 0 14 14"><circle cx="7" cy="7" r="6" fill="none" stroke="var(--white)" stroke-width="1.2"/><ellipse cx="7" cy="7" rx="2.6" ry="6" fill="none" stroke="var(--white)" stroke-width="1"/><path d="M1 7 H13" stroke="var(--white)" stroke-width="1"/></svg>
    www.brightpine365.com
  </div>
</section>

</body>
</html>
```